Munchcart

App Design for a an application on which you can order take aways from restaurants close to you.
(similar app : https://appvault.example/lu/app/grubniq-pizza-burger-sushi/id583017264?l=en&mt=8 )

Logo is a taxi (psd of taxi an font attached)

Attached a draft mockup showing the screens needed.

Screens needed :

1. Splash Screen
2. Select you restaurant screen
3. Select your dish (meat, pizza, pasta....)
4. Select your extras (exta cheese, garlik etc...)
5. Exit screen with total amount and confirmation
6. Subscribe Screen where people have to register the first time.

Target Market(s)

age 14-54

Industry/Entity Type

Restaurant

Requirements
Must have
• Wood elements

```html
<!DOCTYPE html>
<html lang="en">
<head>
<meta charset="utf-8">
<title>Munchcart – Your Order</title>
<link rel="stylesheet" href="https://fonts.googleapis.com/css2?family=Poppins:ital,wght@0,400;0,500;0,600;1,400&family=PT+Sans:wght@700&display=swap">
<style>
  :root {
    --status-bg: #1c1c1c;
    --status-text: #f2f2f2;
    --header-top: #f6f4f0;
    --header-bottom: #dedbd5;
    --button-top: #fbfbfa;
    --button-bottom: #d9d6d0;
    --button-text: #5a5a5a;
    --brand-ink: #1a1a1a;
    --search-yellow: #fbf81c;
    --search-text: #6b5a12;
    --wood-light: #d9b88c;
    --wood-mid: #b98a58;
    --wood-dark: #8e6038;
    --card-yellow: rgba(250, 240, 20, 0.93);
    --card-ink: #5f4f18;
    --card-rule: rgba(110, 90, 30, 0.45);
    --price-red: #d41416;
    --qty-top: #ececec;
    --qty-bottom: #b9b9b9;
    --qty-ink: #111111;
    --icon-olive: #b3a31c;
    --radio-off: #d8d5c6;
    --radio-on: #44d61f;
    --summary-bg: rgba(248, 240, 228, 0.82);
    --summary-ink: #6d5a4c;
    --summary-strong: #6a5140;
  }
  * { box-sizing: border-box; margin: 0; padding: 0; }
  html, body { width: 676px; height: 1200px; overflow: hidden; }
  body { position: relative; font-family: "Poppins", sans-serif; background: var(--wood-mid); }

  .wood-backdrop {
    position: absolute; left: 0; top: 147px; width: 676px; height: 1053px;
    background: linear-gradient(90deg, var(--wood-dark) 0%, var(--wood-light) 12%, var(--wood-mid) 28%, var(--wood-light) 45%, var(--wood-mid) 62%, var(--wood-light) 80%, var(--wood-dark) 100%);
  }

  .status-bar {
    position: absolute; left: 0; top: 0; width: 676px; height: 27px;
    background: var(--status-bg); color: var(--status-text);
    font: 500 14px/27px "Poppins", sans-serif;
  }
  .status-bar .carrier { position: absolute; left: 10px; }
  .status-bar .clock { position: absolute; left: 0; width: 676px; text-align: center; }
  .status-bar .battery { position: absolute; right: 10px; top: 7px; width: 30px; height: 14px; border: 2px solid var(--status-text); border-radius: 3px; }
  .status-bar .battery::after { content: ""; position: absolute; inset: 1px; background: var(--status-text); }

  .app-header {
    position: absolute; left: 0; top: 27px; width: 676px; height: 64px;
    background: linear-gradient(var(--header-top), var(--header-bottom));
  }
  .header-button {
    position: absolute; top: 20px; height: 36px; border-radius: 4px;
    background: linear-gradient(var(--button-top), var(--button-bottom));
    box-shadow: 0 1px 2px rgba(0,0,0,0.35);
    color: var(--button-text); font: 600 21px/36px "Poppins", sans-serif; text-align: center;
  }
  .header-button.list { left: 32px; width: 101px; }
  .header-button.filter { left: 543px; width: 98px; }
  .brand-name {
    position: absolute; left: 0; width: 676px; top: 14px; text-align: center;
    font: 600 30px/40px "Poppins", sans-serif; color: var(--brand-ink);
  }

  .search-bar {
    position: absolute; left: 0; top: 91px; width: 676px; height: 56px;
    background: var(--search-yellow); color: var(--search-text);
    font: 500 18px/56px "Poppins", sans-serif; padding-left: 32px;
    box-shadow: 0 2px 3px rgba(0,0,0,0.25);
  }
  .search-bar svg { position: absolute; right: 28px; top: 22px; }

  .order-card {
    position: absolute; left: 32px; width: 609px; background: var(--card-yellow); color: var(--card-ink);
  }
  .order-card.first { top: 171px; height: 224px; }
  .order-card.second { top: 420px; height: 349px; }
  .dish-title { position: absolute; left: 11px; top: 8px; font: 600 32px/48px "Poppins", sans-serif; }
  .title-rule { position: absolute; left: 11px; right: 11px; top: 50px; border-top: 1px solid var(--card-rule); }
  .dish-desc { position: absolute; left: 11px; top: 68px; font: italic 400 20px/28px "Poppins", sans-serif; }
  .extras { position: absolute; left: 11px; font: 400 25px/34px "Poppins", sans-serif; padding-left: 32px; }
  .extras::before { content: ""; position: absolute; left: 0; top: 9px; width: 18px; height: 18px; border-radius: 50%; background: var(--radio-off); box-shadow: inset 0 -2px 3px rgba(0,0,0,0.2); }
  .extras.on::before { background: var(--radio-on); }
  .extra-list { position: absolute; left: 43px; list-style: none; font: italic 400 20px/32px "Poppins", sans-serif; }
  .extras-rule { position: absolute; left: 11px; width: 454px; border-top: 1px solid var(--card-rule); }
  .price { position: absolute; left: 11px; font: 700 30px/40px "PT Sans", sans-serif; color: var(--price-red); }
  .qty-box {
    position: absolute; left: 501px; width: 98px; height: 88px;
    background: linear-gradient(var(--qty-top), var(--qty-bottom));
    box-shadow: inset 0 0 0 1px rgba(0,0,0,0.15);
    color: var(--qty-ink); font: 500 54px/88px "Poppins", sans-serif; text-align: center;
  }
  .qty-action { position: absolute; }

  .order-summary {
    position: absolute; left: 32px; top: 793px; width: 609px; height: 350px;
    background: var(--summary-bg); color: var(--summary-ink);
  }
  .item-count { position: absolute; left: 16px; top: 20px; font: 400 26px/36px "Poppins", sans-serif; }
  .summary-row { position: absolute; left: 16px; right: 16px; display: flex; justify-content: space-between; align-items: baseline; }
  .summary-row.discount { top: 80px; font: 400 27px/40px "Poppins", sans-serif; }
  .summary-row.total { top: 140px; font: 600 37px/50px "Poppins", sans-serif; color: var(--summary-strong); }
  .summary-row .amount { font-family: "PT Sans", sans-serif; font-weight: 700; color: var(--price-red); font-size: 30px; }
  .summary-rule { position: absolute; left: 10px; right: 10px; top: 207px; border-top: 1px solid rgba(110,90,70,0.45); }
  .pay-button { position: absolute; left: 0; width: 609px; top: 244px; text-align: center; font: 600 39px/52px "Poppins", sans-serif; color: var(--summary-strong); }
</style>
</head>
<body>
  <div class="wood-backdrop" role="img" aria-label="Vertical light wood plank texture background"></div>

  <div class="status-bar">
    <span class="carrier">▂▄▆ NOVA 3G</span>
    <span class="clock">4:20 AM</span>
    <span class="battery"></span>
  </div>

  <header class="app-header">
    <div class="header-button list">List</div>
    <div class="brand-name">Munchcart</div>
    <div class="header-button filter">Filter</div>
  </header>

  <div class="search-bar">Search
    <svg width="13" height="13" viewBox="0 0 13 13"><circle cx="5" cy="5" r="3.8" fill="none" stroke="#6b5a12" stroke-width="1.8"/><line x1="8" y1="8" x2="12" y2="12" stroke="#6b5a12" stroke-width="2"/></svg>
  </div>

  <section class="order-card first">
    <h2 class="dish-title">Beef Wellington with Oyster Pate</h2>
    <div class="title-rule"></div>
    <p class="dish-desc">Simple description goes here</p>
    <div class="extras" style="top:128px">Extras</div>
    <div class="extras-rule" style="top:160px"></div>
    <div class="price" style="top:176px">$18.00</div>
    <div class="qty-box" style="top:73px">1</div>
    <svg class="qty-action" style="left:500px;top:184px" width="24" height="24" viewBox="0 0 24 24"><path d="M12 3v18M3 12h18" stroke="var(--icon-olive)" stroke-width="5"/></svg>
    <svg class="qty-action" style="left:573px;top:186px" width="22" height="22" viewBox="0 0 22 22"><path d="M3 3l16 16M19 3L3 19" stroke="var(--icon-olive)" stroke-width="4.5"/></svg>
  </section>

  <section class="order-card second">
    <h2 class="dish-title">Pizza Pepperoni</h2>
    <div class="title-rule"></div>
    <p class="dish-desc">Simple description goes here</p>
    <div class="extras on" style="top:126px">Extras</div>
    <ul class="extra-list" style="top:172px">
      <li>- Cheese</li>
      <li>- Onion</li>
      <li>- Bacon</li>
    </ul>
    <div class="extras-rule" style="top:284px"></div>
    <div class="price" style="top:300px">$18.00</div>
    <div class="qty-box" style="top:71px">1</div>
    <svg class="qty-action" style="left:500px;top:181px" width="24" height="24" viewBox="0 0 24 24"><path d="M12 3v18M3 12h18" stroke="var(--icon-olive)" stroke-width="5"/></svg>
    <svg class="qty-action" style="left:573px;top:183px" width="22" height="22" viewBox="0 0 22 22"><path d="M3 3l16 16M19 3L3 19" stroke="var(--icon-olive)" stroke-width="4.5"/></svg>
  </section>

  <section class="order-summary">
    <div class="item-count">2 ITEMS + EXTRAS</div>
    <div class="summary-row discount"><span>Discount</span><span class="amount">$0.00</span></div>
    <div class="summary-row total"><span>Total:</span><span class="amount">$36.00</span></div>
    <div class="summary-rule"></div>
    <div class="pay-button">PROCEDD TO PAYMENT</div>
  </section>
</body>
</html>
```